Real Estate Email Signature

I need a professional looking real estate email signature with my picture, logo, and Name, Real Estate Broker/Realtor, and Top of Quorvane logo

```html
<!DOCTYPE html>
<html lang="en">
<head>
<meta charset="utf-8">
<title>Owen Marsh – Email Signature</title>
<link href="https://fonts.googleapis.com/css2?family=Barlow:wght@400;500;600;700&family=Barlow+Semi+Condensed:wght@500&display=swap" rel="stylesheet">
<style>
  :root {
    --bg-charcoal: #3b3b3d;
    --band-navy: #2b3585;
    --icon-blue: #1f5a8c;
    --text-white: #ffffff;
    --text-grey: #b5b7ba;
    --text-light: #e6e7e9;
    --photo-light: #c9d3dc;
    --photo-dark: #7c8a98;
  }
  * { margin: 0; padding: 0; box-sizing: border-box; }
  html, body { width: 1200px; height: 300px; overflow: hidden; background: #ffffff; }
  .signature {
    position: relative;
    width: 1200px;
    height: 300px;
    background: var(--bg-charcoal);
    font-family: "Barlow", Arial, sans-serif;
    overflow: hidden;
  }
  .skyline {
    position: absolute;
    left: 580px; top: 40px;
    width: 380px; height: 196px;
    background: linear-gradient(180deg, rgba(255,255,255,0.01), rgba(255,255,255,0.06));
  }
  .footer-band {
    position: absolute;
    left: 0; top: 236px;
    width: 1200px; height: 64px;
    background: var(--band-navy);
  }
  .portrait { position: absolute; left: 0; top: 0; width: 320px; height: 300px; }
  .brand-mark {
    position: absolute;
    left: 30px; top: 16px;
    width: 68px; height: 68px;
    border-radius: 50%;
    background: var(--icon-blue);
    border: 4px solid var(--text-white);
    color: var(--text-white);
    font-weight: 700;
    font-size: 28px;
    display: flex; align-items: center; justify-content: center;
  }
  .agent-name {
    position: absolute;
    left: 322px; top: 66px;
    font-family: "Barlow Semi Condensed", "Barlow", Arial, sans-serif;
    font-size: 76px; font-weight: 500;
    letter-spacing: 2px;
    color: var(--text-light);
    line-height: 1;
    white-space: nowrap;
  }
  .agent-title {
    position: absolute;
    left: 324px; top: 146px;
    font-size: 28px; font-weight: 400;
    color: var(--text-grey);
  }
  .contact-item {
    position: absolute;
    left: 796px;
    display: flex; align-items: center;
    gap: 20px;
    color: var(--text-light);
  }
  .contact-item.address { top: 70px; }
  .contact-item.phone { top: 146px; }
  .contact-icon {
    width: 44px; height: 44px;
    border-radius: 50%;
    background: var(--icon-blue);
    display: flex; align-items: center; justify-content: center;
    flex-shrink: 0;
  }
  .contact-text { font-size: 25px; line-height: 34px; font-weight: 400; }
  .phone .contact-text { font-weight: 500; }
  .award {
    position: absolute;
    left: 796px; top: 254px;
    display: flex; align-items: center; gap: 10px;
    color: var(--text-white);
    font-size: 20px; font-weight: 700;
    letter-spacing: 1px;
    text-transform: uppercase;
  }
  .award-square { width: 22px; height: 22px; background: var(--text-white); }
</style>
</head>
<body>
  <div class="signature">
    <div class="skyline" role="img" aria-label="Faint city skyline decoration"></div>
    <div class="footer-band"></div>

    <svg class="portrait" viewBox="0 0 320 300" role="img" aria-label="Portrait photo of Owen Marsh">
      <defs>
        <linearGradient id="photoTone" x1="0" y1="0" x2="0" y2="1">
          <stop offset="0" stop-color="#c9d3dc"/>
          <stop offset="1" stop-color="#7c8a98"/>
        </linearGradient>
      </defs>
      <polygon points="155,6 272,64 272,236 155,294 38,236 38,64"
               fill="url(#photoTone)" stroke="#ffffff" stroke-width="8" stroke-linejoin="round"/>
    </svg>

    <div class="brand-mark">LR</div>

    <h1 class="agent-name">OWEN MARSH</h1>
    <p class="agent-title">Director</p>

    <div class="contact-item address">
      <span class="contact-icon">
        <svg width="22" height="26" viewBox="0 0 22 26"><path d="M11 1C5.5 1 2 5 2 9.5 2 16 11 25 11 25s9-9 9-15.5C20 5 16.5 1 11 1z" fill="#fff"/><circle cx="11" cy="9.5" r="3.5" fill="#1f5a8c"/></svg>
      </span>
      <span class="contact-text">4870 Willowbend Court<br>Larkfield, IN 46290</span>
    </div>

    <div class="contact-item phone">
      <span class="contact-icon">
        <svg width="22" height="22" viewBox="0 0 24 24"><path d="M6.6 10.8a15.1 15.1 0 006.6 6.6l2.2-2.2c.3-.3.7-.4 1-.2 1.1.4 2.3.6 3.6.6.6 0 1 .4 1 1V20c0 .6-.4 1-1 1A17 17 0 013 4c0-.6.4-1 1-1h3.5c.6 0 1 .4 1 1 0 1.3.2 2.5.6 3.6.1.3 0 .7-.2 1z" fill="#fff"/></svg>
      </span>
      <span class="contact-text">317-555-0148</span>
    </div>

    <div class="award">
      <span class="award-square"></span>
      <span>Top of Quorvane</span>
    </div>
  </div>
</body>
</html>
```